Bramblefen steakhouse dl flyer

We need a simple dl flyer for our restaurant bramblefen steakhouse. (formerly tildas restaurant at bramblefen lodge, lantern crest mountain, BC Canada)
DL format. double sided. Front Could be the same as poster, back to have additional photos and info.

Perhaps a stock photo of a Plated steak, and people at a bar is also needed.

Target Market(s)

25 to 55 year old skiers, couples, families

Industry/Entity Type

Restaurant

Requirements
Must have
• must tie in with the Bramblefen steakhouse poster.
Nice to have
• warm tones that tie in with the black poster, and flame grilled steak.
Should not have
• bright colours

```html
<!DOCTYPE html>
<html lang="en">
<head>
<meta charset="utf-8">
<title>Bramblefen Steakhouse – DL Flyer</title>
<link rel="stylesheet" href="https://fonts.googleapis.com/css2?family=Cinzel:wght@400&family=Arimo:wght@400&display=swap">
<style>
  :root {
    --paper: #ffffff;
    --ink: #2a2a2a;
    --ink-soft: #3a3a3a;
    --rule: #4a4a4a;
    --photo-dark: #2c2a28;
    --photo-light: #e9e7e4;
    --photo-warm: #c8673a;
  }
  html, body {
    margin: 0;
    padding: 0;
    overflow: hidden;
    background: var(--paper);
  }
  .flyer {
    position: relative;
    width: 1200px;
    height: 2546px;
    background: var(--paper);
    color: var(--ink);
    font-family: "Arimo", Arial, sans-serif;
    overflow: hidden;
  }
  .rule {
    position: absolute;
    left: 181px;
    width: 838px;
    height: 3px;
    background: var(--rule);
  }
  .rule--top { top: 370px; }
  .rule--mid { top: 1008px; }
  .rule--low { top: 1804px; }

  .brand-name {
    position: absolute;
    top: 392px;
    left: 0;
    width: 100%;
    margin: 0;
    text-align: center;
    font-family: "Cinzel", Georgia, serif;
    font-weight: 400;
    font-size: 112px;
    line-height: 112px;
    letter-spacing: 1px;
    color: var(--ink);
  }
  .brand-name span { display: block; }

  .intro {
    position: absolute;
    top: 686px;
    left: 150px;
    width: 900px;
    margin: 0;
    text-align: center;
    font-size: 40px;
    line-height: 51px;
    color: var(--ink-soft);
  }

  .hero-photo {
    position: absolute;
    top: 1098px;
    left: 0;
    width: 1200px;
    height: 630px;
    background:
      radial-gradient(ellipse 32% 38% at 46% 52%, var(--photo-warm) 0%, rgba(200,103,58,0.35) 55%, rgba(200,103,58,0) 100%),
      linear-gradient(180deg, var(--photo-dark) 0%, #6b6661 30%, var(--photo-light) 55%, #d9d6d2 80%, #5a5753 100%);
  }

  .cuisine {
    position: absolute;
    top: 1876px;
    left: 150px;
    width: 900px;
    margin: 0;
    text-align: center;
    font-size: 40px;
    line-height: 52px;
    color: var(--ink-soft);
  }

  .hours {
    position: absolute;
    top: 2132px;
    left: 0;
    width: 100%;
    text-align: center;
    color: var(--ink-soft);
  }
  .hours__title {
    margin: 0 0 16px;
    font-weight: 400;
    font-size: 50px;
    line-height: 60px;
  }
  .hours__list {
    margin: 0;
    font-size: 37px;
    line-height: 51px;
  }
  .hours__note {
    margin: 26px 0 0;
    font-size: 29px;
    line-height: 36px;
  }
</style>
</head>
<body>
  <main class="flyer">
    <h1 class="brand-name"><span>Bramblefen</span><span>Steakhouse</span></h1>
    <div class="rule rule--top"></div>

    <p class="intro">The Bramblefen Steakhouse provides a casual, yet unparalleled mountain dining experience that is inspired by locally sourced food and wines from British Columbia.</p>

    <div class="rule rule--mid"></div>

    <div class="hero-photo" role="img" aria-label="Photo of a plated steak with microgreens on mashed potato, a roasted red pepper and orange sauce on a white square plate"></div>

    <div class="rule rule--low"></div>

    <p class="cuisine">Here you can sample the best of<br>Rocky Mountain Cuisine such as<br>Elk, Bison, Beef and Salmon.</p>

    <section class="hours">
      <h2 class="hours__title">Opening Hours</h2>
      <p class="hours__list">Dinner 5pm to 10pm.<br>Breakfast 7am to 10am</p>
      <p class="hours__note">(Bookings essential for non-house guests)</p>
    </section>
  </main>
</body>
</html>
```